Trading company need to develop packaging design for a new nuts brand.

We need a packaging design for a new nuts brand.
- Packaging format - doypack packaging with zip lock 150 g - 150x220mm
- Product line will include all possible types of nuts. We would like to take a pistachio like an exampl for developing design.
- The main task is to connect the whole concept to the chameleon character /hero (Example of the image is in Uploaded files, but you don't need to use it)
- In design we expect modern, creative and non-standard solutions, we focus on minimalism
- Packaging mustn’t be transparent or craft
- The future product will be a premium segment
- We expect front and back design of packaging
- Our competitors: Tovren and Halvinder (Examples of competitors' packaging, I will attach in Uploaded files)
- Future brand would be sold in different countries therefore the design must be universal, not connect to any region, country or place of nuts growth.

```html
<!DOCTYPE html>
<html lang="en">
<head>
<meta charset="utf-8">
<title>Premium Pistachio – Doypack Front</title>
<link rel="stylesheet" href="https://fonts.googleapis.com/css2?family=Montserrat:wght@400;500;600;700&family=Roboto:wght@500;700&display=swap">
<style>
  :root {
    --stage: #d4d5d8;
    --pouch: #000000;
    --brand-green: #1f6b3a;
    --leaf-green: #7cb82f;
    --band-light: #8fc73e;
    --band-dark: #5e9a26;
    --logo-dot: #a3c97a;
    --nut-light: #e6dcc0;
    --nut-dark: #b9a57a;
    --badge-white: #ffffff;
    --badge-green: #1c6a35;
  }
  html, body {
    margin: 0;
    padding: 0;
    width: 1200px;
    height: 970px;
    overflow: hidden;
    background: var(--stage);
  }
  .canvas {
    position: relative;
    width: 1200px;
    height: 970px;
  }
  .pouch {
    position: absolute;
    left: 387px;
    top: 164px;
    width: 426px;
    height: 642px;
    font-family: "Montserrat", sans-serif;
  }
  .pouch-shape {
    position: absolute;
    inset: 0;
  }
  .brand {
    position: absolute;
    left: 48px;
    top: 96px;
    display: flex;
    align-items: center;
    gap: 9px;
  }
  .brand-dot {
    width: 42px;
    height: 42px;
    border-radius: 50%;
    background: var(--logo-dot);
  }
  .brand-name {
    margin: 0;
    color: var(--brand-green);
    font-weight: 500;
    font-size: 15px;
    line-height: 17px;
    letter-spacing: 5px;
  }
  .mascot {
    position: absolute;
    left: 48px;
    top: 129px;
    width: 285px;
    height: 315px;
    border-radius: 48% 40% 45% 50%;
    background: radial-gradient(circle at 55% 35%, #e3a93f 0%, #d0564a 40%, #8c6bb0 70%, rgba(120,170,60,0.85) 100%);
  }
  .product {
    position: absolute;
    left: 58px;
    top: 466px;
  }
  .product-tier {
    margin: 0;
    color: var(--brand-green);
    font-weight: 600;
    font-size: 17px;
    letter-spacing: 5px;
    line-height: 18px;
  }
  .product-style {
    margin: 0;
    color: var(--brand-green);
    font-weight: 400;
    font-size: 10px;
    letter-spacing: 0.8px;
    line-height: 12px;
  }
  .product-name {
    margin: 2px 0 0 -2px;
    color: var(--leaf-green);
    font-weight: 700;
    font-size: 46px;
    line-height: 46px;
    letter-spacing: -0.5px;
  }
  .cert-badge {
    position: absolute;
    left: 196px;
    top: 442px;
    width: 48px;
    height: 46px;
    border-radius: 9px;
    background: var(--badge-white);
    border: 3px solid var(--leaf-green);
    box-sizing: border-box;
  }
  .nutrition {
    position: absolute;
    left: 60px;
    top: 555px;
    display: flex;
    gap: 7px;
    margin: 0;
    padding: 0;
    list-style: none;
  }
  .nutrient {
    width: 52px;
    border-radius: 6px 6px 14px 14px;
    overflow: hidden;
    border: 1.5px solid var(--badge-white);
    font-family: "Roboto", sans-serif;
    text-align: center;
  }
  .nutrient-label {
    display: block;
    background: var(--badge-white);
    color: #111;
    font-size: 8px;
    font-weight: 700;
    line-height: 13px;
  }
  .nutrient-value {
    display: block;
    background: var(--badge-green);
    color: #fff;
    font-size: 9px;
    font-weight: 700;
    line-height: 14px;
    padding-bottom: 2px;
  }
  .net-weight {
    position: absolute;
    left: 300px;
    top: 566px;
    margin: 0;
    color: var(--brand-green);
    font-weight: 500;
    font-size: 20px;
  }
</style>
</head>
<body>
<main class="canvas">
  <section class="pouch" aria-label="Premium roasted and salted pistachio pouch, front">
    <svg class="pouch-shape" viewBox="0 0 710 1070" width="426" height="642" aria-hidden="true">
      <defs>
        <linearGradient id="band" x1="0" y1="0" x2="1" y2="1">
          <stop offset="0" stop-color="var(--band-light)"/>
          <stop offset="1" stop-color="var(--band-dark)"/>
        </linearGradient>
        <linearGradient id="nuts" x1="0" y1="0" x2="1" y2="1">
          <stop offset="0" stop-color="var(--nut-light)"/>
          <stop offset="1" stop-color="var(--nut-dark)"/>
        </linearGradient>
        <clipPath id="pouch-outline">
          <path d="M30 0 H680 Q710 0 710 40 V1020 Q710 1070 660 1070 H50 Q0 1070 0 1020 V40 Q0 0 30 0 Z"/>
        </clipPath>
      </defs>
      <g clip-path="url(#pouch-outline)">
        <rect width="710" height="1070" fill="var(--pouch)"/>
        <polygon points="710,225 290,595 690,1010 710,1010" fill="url(#band)"/>
      </g>
      <polygon points="0,60 6,66 0,72" fill="var(--stage)"/>
      <polygon points="710,60 704,66 710,72" fill="var(--stage)"/>
      <polygon role="img" aria-label="Photo of roasted pistachios in their shells" points="700,270 318,595 680,960 700,960" fill="url(#nuts)"/>
    </svg>

    <div class="brand">
      <span class="brand-dot"></span>
      <p class="brand-name">YOUR<br>LOGO</p>
    </div>

    <div class="mascot" role="img" aria-label="Geometric multicoloured chameleon illustration with curled tail"></div>

    <div class="cert-badge" role="img" aria-label="Certification badge"></div>

    <div class="product">
      <p class="product-tier">PREMIUM</p>
      <p class="product-style">ROASTED &amp; SALTED</p>
      <h1 class="product-name">PISTACHIO</h1>
    </div>

    <ul class="nutrition">
      <li class="nutrient"><span class="nutrient-label">Cholesterol</span><span class="nutrient-value">0g</span></li>
      <li class="nutrient"><span class="nutrient-label">Trans Fat</span><span class="nutrient-value">0g</span></li>
      <li class="nutrient"><span class="nutrient-label">Protein</span><span class="nutrient-value">11g</span></li>
      <li class="nutrient"><span class="nutrient-label">Fibre</span><span class="nutrient-value">4g</span></li>
    </ul>

    <p class="net-weight">200g</p>
  </section>
</main>
</body>
</html>
```